Business Card and Presentation Folder for Roofing Company
Business Card and Presentation Folder for Roofing Company - Construction
Creative Brief
Professional
Mark Ellis
Field Supervisor
2718 Brennan Ave Suite 310 Larkfield, MO 63199
855-555-SEAL
mellis@slatepeak.example
www.SlatePeakRestoration.example
IL License #207.538142
stay with our colors of Yellow PMS 106, Black, and White
we want Logo Residential & Commercial 314-555-0178 Accredited Member of the QCA with an A+ Rating possible tag line: Everything you need under One Roof! or: Dedicated to being the most Trusted name in the Roofing Industry!
WendySlatePeak WendySlatePeak
COMBINE #217 AND #208 AND I WILL FINALIZE
#216...PLEASE MAKE THE CHANGES I REQUESTED SO I CAN FINALIZE THIS......
I extended the context
I uploaded an example of what I want our 2 presentation folders to look like: commercial folder: the 9 ICONS WILL BE: Flat roof Industrial building, Factory, City Highrise building, Apartment (3 story), Church, Gas Station, Restaurant, Hotel, & Bank Residential Folder: 9 ICONS WILL BE: House, House with flat roof, Condo, Siding, Gutters, Insulation, Ventilation, Storm Damage, Water&Fire Damage (together)
I uploaded our logos. Our colors are Yellow PMS106, Black, and White.....please use only these colors. Need business cards and Presentation Folder 9x12" (standard size) I will need the final files in Photoshop PSD file with all layers visible so I can make any future changes myself. Thanks Wendy

```html
<!DOCTYPE html>
<html lang="en">
<head>
<meta charset="utf-8">
<title>Slate Peak Restoration – Business Card and Presentation Folder</title>
<link rel="stylesheet" href="https://fonts.googleapis.com/css2?family=Montserrat:wght@400;600;800&family=Tinos:wght@400&display=swap">
<style>
:root{
  --yellow:#fedd00;
  --black:#141414;
  --ink:#1d1d1d;
  --white:#ffffff;
  --paper:#f4f4f4;
  --stage:#d9d9d9;
  --muted:#cfcfcf;
  --band:#eaeaea;
}
*{box-sizing:border-box;margin:0;padding:0}
html,body{width:1200px;height:1049px;overflow:hidden}
body{background:var(--stage);font-family:"Montserrat",Arial,sans-serif;position:relative}

.cards-row{position:absolute;left:0;top:0;width:1200px;height:274px;background:var(--band)}
.divider{position:absolute;left:0;top:274px;width:1200px;height:5px;background:var(--white)}

.card{position:absolute;top:12px;width:450px;height:256px;border-radius:16px;overflow:hidden}
.card-front{left:136px;background:var(--black);color:var(--white)}
.card-back{left:612px;background:var(--yellow);color:var(--ink)}

.person{position:absolute;left:28px;top:98px}
.person-name{font-family:"Tinos","Times New Roman",serif;font-size:30px;line-height:1.1;color:var(--yellow)}
.person-role{font-family:"Tinos","Times New Roman",serif;font-size:14px;color:var(--white);margin-top:4px}

.contacts{position:absolute;left:216px;top:44px;list-style:none}
.contacts li{display:flex;align-items:center;gap:7px;font-size:9px;line-height:19px;color:var(--white);white-space:nowrap}
.contacts svg{width:10px;height:10px;flex:none}
.contacts .indent{padding-left:17px}

.front-band{position:absolute;left:0;bottom:0;width:100%;height:36px;background:var(--yellow);display:flex;align-items:center;justify-content:space-between;padding:0 22px 0 28px}
.license{font-size:9px;color:var(--ink)}

.wordmark{display:flex;align-items:center;gap:8px;font-weight:800;text-transform:uppercase;letter-spacing:.02em}
.wordmark .mark-square{flex:none}
.wordmark-small{font-size:11px;color:var(--ink)}
.wordmark-small .mark-square{width:9px;height:9px;background:var(--ink)}

.back-logo{position:absolute;left:0;top:34px;width:100%;justify-content:center;font-size:30px;color:var(--ink);line-height:1.05;text-align:center}
.back-logo .mark-square{width:24px;height:24px;background:var(--ink)}
.back-band{position:absolute;left:0;top:152px;width:100%;height:48px;background:var(--black);color:var(--white);text-align:center;font-family:"Tinos","Times New Roman",serif;font-size:12.5px;line-height:18px;padding-top:6px}
.tagline{position:absolute;left:0;top:220px;width:100%;text-align:center;font-family:"Tinos","Times New Roman",serif;font-size:10.5px;color:var(--ink)}

.folder-cover{position:absolute;left:92px;top:440px;width:440px;height:596px;background:var(--black);overflow:hidden}
.cover-logo{position:absolute;left:0;top:104px;width:100%;justify-content:center;font-size:40px;color:var(--yellow);text-align:center;line-height:1.05}
.cover-logo .mark-square{width:34px;height:34px;background:var(--yellow)}
.cover-stripe{position:absolute;left:0;width:100%;background:var(--yellow)}
.stripe-thin{bottom:30px;height:4px}
.stripe-wide{bottom:10px;height:14px}
.cover-foot{position:absolute;right:22px;bottom:42px;font-size:12px;color:var(--yellow)}
.cover-foot .mark-square{width:10px;height:10px;background:var(--yellow)}

.folder-inside{position:absolute;left:582px;top:384px;width:512px;height:640px;background:var(--paper);overflow:hidden}
.inside-fold{position:absolute;left:0;top:0;width:2px;height:100%;background:var(--muted)}
.inside-pocket{position:absolute;left:0;bottom:0;width:100%;height:320px}
</style>
</head>
<body>

<section class="cards-row">
  <article class="card card-front">
    <div class="person">
      <p class="person-name">Mark Ellis</p>
      <p class="person-role">Field Supervisor</p>
    </div>
    <ul class="contacts">
      <li><svg viewBox="0 0 10 10"><circle cx="5" cy="5" r="5" fill="#fedd00"/></svg>855-555-SEAL (Toll Free)</li>
      <li><svg viewBox="0 0 10 10"><circle cx="5" cy="5" r="5" fill="#fedd00"/></svg>314-555-0178</li>
      <li><svg viewBox="0 0 10 10"><circle cx="5" cy="5" r="5" fill="#fedd00"/></svg>314-555-0142</li>
      <li><svg viewBox="0 0 10 10"><circle cx="5" cy="5" r="5" fill="#fedd00"/></svg>314-555-0196</li>
      <li><svg viewBox="0 0 10 10"><circle cx="5" cy="5" r="5" fill="#fedd00"/></svg>mellis@slatepeak.example</li>
      <li><svg viewBox="0 0 10 10"><circle cx="5" cy="5" r="5" fill="#fedd00"/></svg>www.SlatePeakRestoration.example</li>
      <li><svg viewBox="0 0 10 10"><circle cx="5" cy="5" r="5" fill="#fedd00"/></svg>2718 Brennan Ave Suite 310 Larkfield,</li>
      <li class="indent">MO 63199</li>
    </ul>
    <div class="front-band">
      <span class="license">License #207.538142</span>
      <span class="wordmark wordmark-small"><span class="mark-square"></span>Slate Peak</span>
    </div>
  </article>

  <article class="card card-back">
    <div class="wordmark back-logo"><span class="mark-square"></span><span>Slate Peak<br>Restoration</span></div>
    <div class="back-band">
      Residential &amp; Commercial : 314-555-0178<br>
      Accredited Member of the QCA with an A+ Rating
    </div>
    <p class="tagline">Dedicated to Being the most Trusted name in the Roofing Industry!</p>
  </article>
</section>
<div class="divider"></div>

<section class="folder-cover">
  <div class="wordmark cover-logo"><span class="mark-square"></span><span>Slate Peak<br>Restoration</span></div>
  <div class="wordmark cover-foot"><span class="mark-square"></span>Slate Peak</div>
  <div class="cover-stripe stripe-thin"></div>
  <div class="cover-stripe stripe-wide"></div>
</section>

<section class="folder-inside">
  <div class="inside-fold"></div>
  <svg class="inside-pocket" viewBox="0 0 512 320" preserveAspectRatio="none">
    <path d="M0 30 L512 0 L512 320 L0 320 Z" fill="#141414"/>
    <path d="M400 6 Q430 60 480 60 L512 58 L512 0 Z" fill="#2a2a2a"/>
  </svg>
</section>

</body>
</html>
```